Weight Loss water drink label for "Golden Reed Glow" drinks

We need a label design for our new exciting water based weight loss drink called " Golden Reed Glow " weight loss water. It is a carb blocking, calorie burning health drink that assists in weight loss amongst men and woman. The drink is 100% natural with no sugar added. The drink comes in flavours like refreshing lemon, tropical berry and smooth strawberry. The label is for a 500ml bottle and needs to incorporate text on the label. I have uploaded a previous design to the task but feel free to be creative if you have a better idea. the label needs to stand out in the crowd and also be simple and use colour. The label has to appeal to the general public.

Target Market(s)

Our target market is men and woman between the ages of 18 and 65 that are either interested in losing weight or a living healthy

Industry/Entity Type

Health And Wellness

Font styles to use
Script

Requirements
Must have
• Must have the title " Golden Reed Glow " weight loss drink on the label as the title
• Must be a complete label design for a 500ml water bottle.
• Must have colour
• Must be unique
Nice to have
• The shape of a man and a woman's in shape physique as part of the label, not the same shapes used in the uploaded design, must look more details.
Should not have
• No colour or creativity

```html
<!DOCTYPE html>
<html lang="en">
<head>
<meta charset="utf-8">
<title>Golden Reed Glow – Weight Loss Water Labels</title>
<link rel="stylesheet" href="https://fonts.googleapis.com/css2?family=Oswald:wght@600;700&family=Archivo+Narrow:wght@400;600;700&display=swap">
<style>
:root{
  --stage:#0d0d0d;
  --paper:#ffffff;
  --ink:#111111;
  --berry:#4d5f8e;
  --lemon:#f2d51a;
  --strawberry:#e31b23;
  --water-1:rgba(170,200,225,.55);
  --water-2:rgba(220,235,245,.15);
  --muted:#555555;
}
*{box-sizing:border-box;margin:0;padding:0}
html,body{width:1200px;height:846px;overflow:hidden;background:var(--stage)}
.canvas{position:relative;width:1200px;height:846px;background:var(--stage);font-family:"Archivo Narrow",Arial,sans-serif;color:var(--ink)}
.label{position:absolute;background:var(--paper);overflow:hidden}
.label--small{width:184px;height:397px;top:368px}
.label--large{width:223px;height:472px;top:254px}
.label--berry{left:97px;--accent:var(--berry)}
.label--lemon{left:375px;--accent:var(--lemon)}
.label--strawberry{left:634px;--accent:var(--strawberry)}
.label--back{left:934px;--accent:var(--strawberry)}

.splash{position:absolute;left:18px;top:0;width:60px;height:100%;
  background:linear-gradient(90deg,var(--water-2),var(--water-1) 45%,var(--water-2));opacity:.8}
.bubbles{position:absolute;right:0;bottom:40px;width:55%;height:90px;
  background:radial-gradient(ellipse at 40% 60%,var(--water-1),transparent 70%)}

.brand{position:absolute;font-family:"Oswald",Impact,sans-serif;font-weight:700;color:var(--accent);text-transform:uppercase;line-height:.95;text-align:center}
.label--small .brand{left:20px;right:20px;top:60px;font-size:30px}
.label--large .brand{left:18px;right:18px;top:80px;font-size:40px}
.brand__mark{display:inline-block;width:14px;height:14px;background:var(--accent);margin-bottom:6px}

.tagline{position:absolute;left:0;right:0;font-size:7.5px;font-weight:700;letter-spacing:.2px;text-align:center}
.label--small .tagline{top:180px}
.label--large .tagline{top:218px;left:14px;text-align:left}

.fruit{position:absolute;border-radius:40%}
.label--small .fruit{left:58px;top:296px;width:74px;height:44px}
.label--large .fruit{left:64px;top:348px;width:70px;height:60px}
.label--berry .fruit{background:linear-gradient(135deg,#c2283a,#2b2b55 60%,#3a4f9a)}
.label--lemon .fruit{background:linear-gradient(135deg,#7fb33a,#f6d21c 40%,#f3e27a)}
.label--strawberry .fruit{background:linear-gradient(135deg,#4f9a2f,#d9201f 45%,#b0151a)}

.band{position:absolute;left:0;right:0;background:var(--accent);color:#111;font-weight:700;letter-spacing:2px;text-align:center}
.label--small .band{top:340px;height:18px;font-size:11px;line-height:18px}
.label--berry .band{color:var(--paper)}
.label--large .band{top:410px;height:21px;font-size:13px;line-height:21px;left:4px;right:6px;color:var(--ink)}
.label--back .band{display:flex;justify-content:space-around;letter-spacing:0;font-weight:400;font-size:15px;color:var(--paper)}

.rule{position:absolute;left:0;right:0;top:362px;border-top:1.5px solid var(--ink)}
.volume{position:absolute;left:0;right:0;font-size:10px;text-align:center;color:var(--muted)}
.label--small .volume{top:378px}
.label--large .volume{top:452px}

.mini-brand{position:absolute;left:20px;top:18px;width:50px;font-family:"Oswald",Impact,sans-serif;font-weight:700;font-size:11px;line-height:1;color:var(--accent);text-transform:uppercase;text-align:center}

.facts{position:absolute;left:70px;top:80px;width:136px;border:1.5px solid var(--ink);padding:3px 4px;font-size:5.2px;line-height:1.35;background:var(--paper)}
.facts__title{font-size:7.5px;font-weight:700;border-bottom:1px solid var(--ink);padding-bottom:2px;margin-bottom:2px}
.facts__head{border-bottom:3px solid var(--ink);padding-bottom:2px}
.facts table{width:100%;border-collapse:collapse}
.facts td{border-bottom:.6px solid var(--ink);padding:1px 0;font-weight:600}
.facts td:last-child{text-align:right}
.facts .indent{padding-left:5px}
.facts .thick td{border-bottom:3px solid var(--ink)}
.facts__note{margin-top:3px}
</style>
</head>
<body>
<main class="canvas">

  <section class="label label--small label--berry">
    <div class="splash" role="img" aria-label="Water splash photograph"></div>
    <div class="bubbles" role="img" aria-label="Water bubbles"></div>
    <h2 class="brand"><span class="brand__mark"></span><br>Golden<br>Reed<br>Glow</h2>
    <p class="tagline">HELPS YOUR BODY TURN FAT INTO ENERGY</p>
    <div class="fruit" role="img" aria-label="Mixed berries photograph"></div>
    <p class="band">weight loss water</p>
    <div class="rule"></div>
    <p class="volume">500ml</p>
  </section>

  <section class="label label--small label--lemon">
    <div class="splash" role="img" aria-label="Water splash photograph"></div>
    <div class="bubbles" role="img" aria-label="Water bubbles"></div>
    <h2 class="brand"><span class="brand__mark"></span><br>Golden<br>Reed<br>Glow</h2>
    <p class="tagline">HELPS YOUR BODY TURN FAT INTO ENERGY</p>
    <div class="fruit" role="img" aria-label="Sliced lemon photograph"></div>
    <p class="band">weight loss water</p>
    <div class="rule"></div>
    <p class="volume">500ml</p>
  </section>

  <section class="label label--large label--strawberry">
    <div class="splash" role="img" aria-label="Water splash photograph"></div>
    <div class="bubbles" role="img" aria-label="Water bubbles"></div>
    <h2 class="brand">Golden<br>Reed<br>Glow</h2>
    <p class="tagline">HELPS YOUR BODY TURN FAT INTO ENERGY</p>
    <div class="fruit" role="img" aria-label="Strawberries with leaves photograph"></div>
    <p class="band">weight loss water</p>
    <p class="volume">500ml</p>
  </section>

  <section class="label label--large label--back">
    <div class="splash" role="img" aria-label="Water splash photograph"></div>
    <p class="mini-brand">Golden<br>Reed<br>Glow</p>
    <div class="facts">
      <p class="facts__title">Nutrition Facts/Datos de Nutrición</p>
      <div class="facts__head">
        <p>Serving Size/Tamaño por Ración</p>
        <p>10.5 fl.oz.(310ml)</p>
        <p>Serving Per Container/ Raciones por Envase 1</p>
      </div>
      <table>
        <tr><td colspan="2">Amount Per Serving/ Cantidad por Ración</td></tr>
        <tr><td colspan="2">Calories/ Calorías 110</td></tr>
        <tr><td colspan="2">Calories from Fat/ Calorías de Grasa 10</td></tr>
        <tr><td>% Daily Value */ Valor Diario*</td><td></td></tr>
        <tr><td>Total Fat/ Grasa Total 1g</td><td>2 %</td></tr>
        <tr><td class="indent">Saturated Fat/ Grasa Saturada 1g</td><td>5 %</td></tr>
        <tr><td class="indent">Trans Fat/Grasa Trans 0g</td><td></td></tr>
        <tr><td>Cholesterol/ Colesterol 0mg</td><td>0 %</td></tr>
        <tr><td>Sodium/Sodio 50mg</td><td>2 %</td></tr>
        <tr><td>Total Carbohydrate/<br>Carbidrato Total 26g</td><td>9 %</td></tr>
        <tr><td class="indent">Dietary Fiber/ Fibra Dietética 0g</td><td>%</td></tr>
        <tr><td class="indent">Sugars/ Azúcares 23g</td><td>%</td></tr>
        <tr class="thick"><td>Protein/ Proteína 0g</td><td>%</td></tr>
        <tr><td>Vitamin A/ Vitamina A</td><td>0 %</td></tr>
        <tr><td>Vitamin C/ Vitamina C</td><td>10%</td></tr>
        <tr><td>Calcium/ Calcio</td><td>3 %</td></tr>
        <tr><td>Iron/Hierro</td><td>2 %</td></tr>
      </table>
      <p class="facts__note">* Percent Daily Values are based on a 2,000 calorie diet./Los Porcentajes de Valorés Diarios estan basados en una dieta de 2,000 calorías.</p>
    </div>
    <p class="band"><span>100% natural</span><span>no sugar</span></p>
  </section>

</main>
</body>
</html>
```